'TOLVANTA' NEW WINE LABEL DESIGN

I am looking for an exceptional and exciting design for a wine label called 'Tolvanta' meaning 'Lookout'. The design must feature the name 'Tolvanta', and the word 'Cabernet Sauvignon' in version 1 and 'Sauvignon Blanc' in version 2. It will also need the words 'Valle Central, Chile' at the bottom of the label as a prominent piece of information as well as the vintage 2017. Please produce the work in size 80mm x 100mm. Feel free to use colour in addition to black/white and ensue that the label is easy to read on a shelf placement.
Target Market(s)
SUPERMARKETS & WINE STORES
Requirements
Must have
- EASY TO READ, USE COLOURS LIKE GREEN FOR SAUVIGNON & RED FOR CABERNET SAUVIGNON
- FULL BOTTLE SHOT MUST BE IN PROVIDED DESIGNS. ALL BOTTLE TOPS SHOULD BE QUORLAN STYLE (SCREW TOP)
- PLEASE NOTE THAT LABEL INFORMATION MUSY BE EASY TO READ I.E. VINTAGE, PLACE OF ORGIN ALTHOUGH NOT THE MAIN CONTENT MUST STILL BE CLEAR.
Nice to have
- ARTISTIC REFERENCE LINK TO NAME & ANDES BUT NOT PICTURES OF MOUNTAINS
Should not have
- PICTURES OF GRAPES
- PICTURES OF VINEYARDS
- PICTURES OF MOUNTAINS

```html
<!DOCTYPE html>
<html lang="en">
<head>
<meta charset="utf-8">
<title>Tolvanta — Cabernet Sauvignon and Sauvignon Blanc labels</title>
<link rel="stylesheet" href="https://fonts.googleapis.com/css2?family=Cinzel:wght@400;600;700&display=swap">
<style>
  :root {
    --backdrop: #f3e6cf;
    --label-light: #e0e0e0;
    --label-dark: #141414;
    --label-dark-soft: #2a2a2a;
    --wine-red: #d3000e;
    --wine-green: #3fae3a;
    --ink-light: #e8e8e8;
    --weave-teal: #1fa58c;
    --weave-green: #4cb848;
    --weave-orange: #f0782a;
    --weave-yellow: #f2c21b;
    --weave-blue: #2a5fb8;
  }
  * { box-sizing: border-box; margin: 0; padding: 0; }
  html, body {
    width: 931px; height: 1200px; overflow: hidden;
    background: var(--backdrop);
  }
  .canvas {
    position: relative; width: 931px; height: 1200px;
    display: flex; justify-content: center; align-items: center; gap: 43px;
  }
  .label {
    position: relative; width: 400px; height: 566px;
    background: var(--label-light);
    overflow: hidden;
    box-shadow: 0 8px 24px rgba(80, 50, 20, 0.18);
    font-family: "Cinzel", serif;
  }
  .label-art { position: absolute; inset: 0; width: 400px; height: 566px; }
  .label-text { position: absolute; left: 0; right: 0; text-align: center; white-space: nowrap; }
  .vintage { font-size: 25px; font-weight: 400; letter-spacing: 1px; }
  .brand { font-size: 36px; font-weight: 600; letter-spacing: 9px; }
  .varietal { font-size: 24px; font-weight: 700; letter-spacing: 0.5px; }
  .origin { color: var(--ink-light); font-size: 17px; font-weight: 400; letter-spacing: 1.5px; }
  .label--cabernet .vintage,
  .label--cabernet .brand,
  .label--cabernet .varietal { color: var(--wine-red); }
  .label--blanc .vintage,
  .label--blanc .varietal { color: var(--wine-green); }
  .label--blanc .brand { color: var(--wine-red); }
</style>
</head>
<body>
<main class="canvas">

  <!-- Cabernet Sauvignon: light top, corner weave -->
  <section class="label label--cabernet">
    <svg class="label-art" viewBox="0 0 400 566" aria-hidden="true">
      <defs>
        <radialGradient id="darkFieldCab" cx="50%" cy="65%" r="70%">
          <stop offset="0" stop-color="var(--label-dark-soft)"/>
          <stop offset="1" stop-color="var(--label-dark)"/>
        </radialGradient>
        <linearGradient id="weaveCab" x1="0" y1="1" x2="1" y2="0">
          <stop offset="0" stop-color="var(--weave-orange)"/>
          <stop offset="0.35" stop-color="var(--weave-yellow)"/>
          <stop offset="0.65" stop-color="var(--weave-teal)"/>
          <stop offset="1" stop-color="var(--weave-blue)"/>
        </linearGradient>
      </defs>
      <path fill="url(#darkFieldCab)" d="M0 258 Q220 270 400 178 L400 566 L0 566 Z"/>
    </svg>
    <svg class="label-art" viewBox="0 0 400 566" role="img" aria-label="Woven Andean textile pattern in orange, yellow, teal and blue">
      <polygon fill="url(#weaveCab)" points="187,566 400,358 400,566"/>
    </svg>
    <p class="label-text vintage" style="top:48px;">2017.</p>
    <p class="label-text brand" style="top:150px;">TOLVANTA</p>
    <p class="label-text varietal" style="top:338px;">CABERNET SAUVIGNON</p>
    <p class="label-text origin" style="top:380px;">VALLE CENTRAL, CHILE</p>
  </section>

  <!-- Sauvignon Blanc: dark field, band weave, green accents -->
  <section class="label label--blanc">
    <svg class="label-art" viewBox="0 0 400 566" aria-hidden="true">
      <defs>
        <radialGradient id="darkFieldBlanc" cx="50%" cy="50%" r="70%">
          <stop offset="0" stop-color="var(--label-dark-soft)"/>
          <stop offset="1" stop-color="var(--label-dark)"/>
        </radialGradient>
        <linearGradient id="weaveBlanc" x1="0" y1="0" x2="0" y2="1">
          <stop offset="0" stop-color="var(--weave-yellow)"/>
          <stop offset="0.35" stop-color="var(--weave-green)"/>
          <stop offset="1" stop-color="var(--weave-teal)"/>
        </linearGradient>
      </defs>
      <path fill="url(#darkFieldBlanc)" d="M0 106 Q220 118 400 42 L400 566 L0 566 Z"/>
    </svg>
    <svg class="label-art" viewBox="0 0 400 566" role="img" aria-label="Woven Andean textile band in yellow, green and teal">
      <rect fill="url(#weaveBlanc)" x="0" y="462" width="400" height="104"/>
    </svg>
    <p class="label-text brand" style="top:163px;">TOLVANTA</p>
    <p class="label-text varietal" style="top:280px;">SAUVIGNON BLANC</p>
    <p class="label-text origin" style="top:320px;">VALLE CENTRAL, CHILE</p>
    <p class="label-text vintage" style="top:410px;">2017.</p>
  </section>

</main>
</body>
</html>
```